Flyer-Design für Hotel mit Halbpension
Obwohl ich keine Ahnung hatte von Design hat Sie mir wirklich gut mit Allem geholfen. Sehr schnell Service bei jeder Frage. Vielen Dank
Zielgruppe
Hotel /Restaurant
Aufgabenstellung
Wir haben bis jetzt nur Halbpension für unsere Hausgäste gemacht, aber wir möchten dass ab Ostern auch gerne für andere Gäste machen.
Unsere Spezialitäten sind Schmorgerichte und Spareribs.
Alles für ein fester Preis: 3-Gänge 18,90, 2 Gänge 15,90, 1 Gang 12,90.
Jeden Sonntag soll es auserdem Schnitzeltag sein: € 6,99 für ein Schnitzel mit Pommer und Salat. Sauce € 1,00 extra.
Folgende Texte sollen in den Flyer:
Vorderseite:
Neu in Manderscheid:
Restaurant im Hotel am Birkenhain
Ab Ostern bis Ende Oktober.
Probieren Sie unsere Spezialitäten:
Schmorgerichte
Ofengerichte (Fisch, FIeisch, Vegetarisch)
Schnitzel
Spare-ribs
Geöffnet von 18:30 bis 20:00 Uhr.
Montag und Dienstag nur Hausgäste.
Rückseite:
Unser Sonderangebot am Sonntag
Von 12:00 bis 20:00 Uhr.
Schweineschnitzel 'Wiener Art' 200 Gr. mit Pommes und Salat.
Pro Perzon: € 6,99
Extra Div. Saucen: € 2,00 Aufpreis

```html
<!DOCTYPE html>
<html lang="de">
<head>
<meta charset="utf-8">
<title>Flyer – Restaurant im Hotel am Birkenhain</title>
<link rel="stylesheet" href="https://fonts.googleapis.com/css2?family=Oswald:wght@400;500;600&family=Roboto+Condensed:wght@400;700&display=swap">
<style>
  :root{
    --green:#4aa33c;
    --green-dark:#3a8a2e;
    --ink:#262a27;
    --band:#252826;
    --paper:#ffffff;
    --bg:#e3e3e3;
    --muted:#555;
  }
  *{box-sizing:border-box;margin:0;padding:0}
  html,body{width:1200px;height:2574px;overflow:hidden;background:var(--bg)}
  body{position:relative;font-family:"Roboto Condensed",sans-serif;color:var(--ink)}
  .flyer{position:absolute;left:200px;width:800px;height:1131px;background:var(--paper);overflow:hidden;box-shadow:0 6px 24px rgba(0,0,0,.18)}
  .flyer--front{top:100px}
  .flyer--back{top:1311px}
  .flyer__topline{position:absolute;left:0;top:0;width:100%;height:8px;background:var(--green)}
  .abs{position:absolute}
  .photo{position:absolute;border-radius:0 0 0 40px}
  .tag{position:absolute;background:var(--green);color:#fff;font-family:"Oswald",sans-serif;font-weight:400;text-transform:uppercase;padding:6px 16px;font-size:24px;letter-spacing:.5px;white-space:nowrap}
  .pill{position:absolute;background:var(--green);color:#fff;font-family:"Oswald",sans-serif;font-size:22px;padding:6px 26px;border-radius:22px;white-space:nowrap;z-index:3}
  .badge{position:absolute;z-index:4}
  .badge svg{position:absolute;inset:0;width:100%;height:100%}
  .badge__text{position:absolute;inset:0;display:flex;flex-direction:column;align-items:center;justify-content:center;color:#fff;font-family:"Oswald",sans-serif;text-transform:uppercase;text-align:center;line-height:1.1}
  .badge__small{font-size:12px;text-transform:none}
  .headline{position:absolute;font-family:"Oswald",sans-serif;color:var(--green);text-transform:uppercase;white-space:nowrap}
  .rule{position:absolute;height:2px;background:var(--green)}
  .menu-label{position:absolute;font-family:"Oswald",sans-serif;color:var(--green);text-transform:uppercase;font-size:20px;white-space:nowrap;z-index:2}
  .landscape{position:absolute;left:0;top:640px;width:800px;height:420px;background:linear-gradient(180deg,#ffffff 0%,#9cc47a 18%,#4e8a36 50%,#2f6a24 100%);z-index:1}
  .dish{position:absolute;width:220px;height:150px;border-radius:14px;box-shadow:0 4px 10px rgba(0,0,0,.3);z-index:3}
  .note{position:absolute;background:#fff;box-shadow:0 6px 16px rgba(0,0,0,.28);text-align:center;font-family:"Oswald",sans-serif;text-transform:uppercase;z-index:2}
  .note__bar{position:absolute;left:-10px;top:-14px;width:16px;height:56px;background:var(--green)}
  .note__lead{color:var(--green);font-size:18px;line-height:1.25}
  .note__item{font-size:18px;line-height:1.25;color:var(--ink)}
  .note__sub{font-family:"Roboto Condensed",sans-serif;text-transform:none;font-size:13px}
  .note__rule{width:60%;height:2px;background:var(--ink);margin:10px auto}
  .band{position:absolute;left:0;width:100%;background:var(--band);color:#fff;z-index:2}
  .icon{width:18px;height:18px;flex:none}
  .info-line{display:flex;align-items:center;gap:10px;font-size:16px;color:#e8e8e8;white-space:nowrap}
  .hours-box{position:absolute;background:var(--band);color:#ddd;font-size:16px;line-height:1.5;padding:20px 22px;display:flex;gap:12px}
</style>
</head>
<body>

<!-- FRONT -->
<section class="flyer flyer--front">
  <div class="flyer__topline"></div>
  <div class="photo" style="left:40px;top:30px;width:720px;height:300px;background:linear-gradient(180deg,#8fb3de 0%,#c9d3da 35%,#d8d6cf 60%,#8a8a86 100%)" role="img" aria-label="Foto: Hotelgebäude mit Terrasse an der Straße in Manderscheid"></div>
  <div class="tag" style="left:40px;top:26px">Neu in Manderscheid</div>
  <div class="badge" style="left:610px;top:265px;width:150px;height:150px">
    <svg viewBox="-50 -50 100 100"><g fill="var(--green)"><rect x="-36" y="-36" width="72" height="72"/><rect x="-36" y="-36" width="72" height="72" transform="rotate(30)"/><rect x="-36" y="-36" width="72" height="72" transform="rotate(60)"/></g></svg>
    <div class="badge__text" style="font-size:17px">Restaurant<br>im Hotel am<br>Birkenhain</div>
  </div>

  <div class="rule" style="left:40px;top:372px;width:130px"></div>
  <div class="headline" style="left:180px;top:348px;font-size:36px">Unsere Spezialitäten</div>
  <div class="rule" style="left:510px;top:372px;width:90px"></div>
  <div class="abs" style="left:40px;top:402px;width:720px;font-size:14px;white-space:nowrap">gekennzeichnete Speisen sind als 1-Gang Menü, 2-Gänge Menü, 3-Gänge Menü zum Festpreis erhältlich</div>

  <div class="menu-label" style="left:50px;top:430px">1-Gang Menüs</div>
  <div class="dish" style="left:40px;top:462px;background:radial-gradient(circle at 40% 50%,#8a5a3a,#3b3a2a 60%,#5a3b5a)" role="img" aria-label="Foto: bunte Schmorgerichte in Schalen"></div>
  <div class="badge" style="left:222px;top:456px;width:60px;height:60px"><svg viewBox="-50 -50 100 100"><g fill="var(--green)"><rect x="-36" y="-36" width="72" height="72"/><rect x="-36" y="-36" width="72" height="72" transform="rotate(30)"/><rect x="-36" y="-36" width="72" height="72" transform="rotate(60)"/></g></svg><div class="badge__text"><span class="badge__small">je</span><span style="font-size:15px">12,90€</span></div></div>

  <div class="menu-label" style="left:300px;top:470px">2-Gänge Menüs</div>
  <div class="dish" style="left:290px;top:502px;background:linear-gradient(135deg,#2b2a22,#7a3a1e 50%,#3a2a1e)" role="img" aria-label="Foto: Spare Ribs auf Holzbrett"></div>
  <div class="badge" style="left:472px;top:496px;width:60px;height:60px"><svg viewBox="-50 -50 100 100"><g fill="var(--green)"><rect x="-36" y="-36" width="72" height="72"/><rect x="-36" y="-36" width="72" height="72" transform="rotate(30)"/><rect x="-36" y="-36" width="72" height="72" transform="rotate(60)"/></g></svg><div class="badge__text"><span class="badge__small">je</span><span style="font-size:15px">15,90€</span></div></div>

  <div class="menu-label" style="left:550px;top:510px">3-Gänge Menüs</div>
  <div class="dish" style="left:540px;top:542px;background:radial-gradient(circle at 55% 50%,#b8325a,#6a3a2a 45%,#8a8a88)" role="img" aria-label="Foto: Fleischgericht mit Beilage auf Teller"></div>
  <div class="badge" style="left:722px;top:536px;width:60px;height:60px"><svg viewBox="-50 -50 100 100"><g fill="var(--green)"><rect x="-36" y="-36" width="72" height="72"/><rect x="-36" y="-36" width="72" height="72" transform="rotate(30)"/><rect x="-36" y="-36" width="72" height="72" transform="rotate(60)"/></g></svg><div class="badge__text"><span class="badge__small">je</span><span style="font-size:15px">18,90€</span></div></div>

  <div class="landscape" role="img" aria-label="Foto: bewaldetes Tal mit Burgruine"></div>

  <div class="note" style="left:60px;top:700px;width:250px;padding:26px 18px">
    <div class="note__bar"></div>
    <div class="note__lead">Probieren Sie<br>unsere Spezialitäten</div>
    <div class="note__rule"></div>
    <div class="note__item">Schmorgerichte</div>
    <div class="note__item" style="margin-top:10px">Ofengerichte</div>
    <div class="note__sub">(Fisch, Fleisch, Vegetarisch)</div>
    <div class="note__item" style="margin-top:10px">Schnitzel</div>
    <div class="note__item" style="margin-top:10px">Spare Ribs</div>
  </div>

  <div class="pill" style="left:270px;top:1040px">Ab Ostern bis Ende Oktober</div>
  <div class="band" style="top:1060px;height:71px;display:flex;align-items:center;padding:0 40px">
    <div class="info-line">
      <svg class="icon" viewBox="0 0 20 20"><circle cx="10" cy="10" r="8" fill="none" stroke="#fff" stroke-width="2"/><path d="M10 5v5h4" fill="none" stroke="#fff" stroke-width="2"/></svg>
      Öffnungszeiten Küche: Mo-Di: nur für Hausgäste &nbsp;|&nbsp; Mi-Do-Fr: 17:30 - 20:00 Uhr &nbsp;|&nbsp; Sa-So: 12:00 - 20:00 Uhr
    </div>
  </div>
</section>

<!-- BACK -->
<section class="flyer flyer--back">
  <div class="flyer__topline"></div>
  <div class="photo" style="left:40px;top:30px;width:720px;height:400px;background:radial-gradient(ellipse at 35% 60%,#c98a3a 0%,#a86a2a 30%,#e8c860 55%,#e9e2d0 80%)" role="img" aria-label="Foto: paniertes Schnitzel mit Pommes, Zitrone und Petersilie"></div>
  <div class="tag" style="left:40px;top:26px">Sonntag ist Schnitzeltag</div>

  <div class="note" style="left:80px;top:490px;width:380px;padding:30px 24px">
    <div class="note__bar"></div>
    <div class="note__lead" style="font-size:22px">Unser Sonderangebot<br>am Sonntag</div>
    <div class="note__rule"></div>
    <div class="note__item" style="font-size:24px">Schweineschnitzel<br>„Wiener Art“ 200 Gramm</div>
    <div class="note__item" style="font-size:24px;margin-top:16px">mit Pommes<br>und Salat</div>
    <div class="note__item" style="font-size:17px;text-transform:none;margin-top:16px">Extra: Diverse Soßen: 2,00€ Aufpreis</div>
  </div>
  <div class="badge" style="left:410px;top:460px;width:90px;height:90px"><svg viewBox="-50 -50 100 100"><g fill="var(--green)"><rect x="-36" y="-36" width="72" height="72"/><rect x="-36" y="-36" width="72" height="72" transform="rotate(30)"/><rect x="-36" y="-36" width="72" height="72" transform="rotate(60)"/></g></svg><div class="badge__text"><span class="badge__small">je</span><span style="font-size:22px">6,90€</span></div></div>

  <div class="pill" style="left:500px;top:520px;font-size:19px;padding:5px 18px">Ab Ostern bis Ende Oktober</div>
  <div class="hours-box" style="left:500px;top:540px;width:260px;height:160px;padding-top:34px">
    <svg class="icon" viewBox="0 0 20 20"><circle cx="10" cy="10" r="8" fill="none" stroke="#fff" stroke-width="2"/><path d="M10 5v5h4" fill="none" stroke="#fff" stroke-width="2"/></svg>
    <div>Öffnungszeiten Küche:<br>Mo-Di: nur für Hausgäste<br>Mi-Do-Fr: 17:30 - 20:00 Uhr<br>Sa-So: 12:00 - 20:00 Uhr</div>
  </div>

  <div class="abs" style="left:510px;top:730px;width:200px;height:140px;border-radius:10px;box-shadow:0 4px 10px rgba(0,0,0,.3);background:linear-gradient(180deg,#8fb3de 0%,#d6d6d0 50%,#8a8a86 100%);z-index:2" role="img" aria-label="Foto: Hotelgebäude"></div>

  <div class="band" style="top:930px;height:201px">
    <div class="abs" style="left:40px;top:40px">
      <div class="info-line" style="align-items:flex-start">
        <svg class="icon" viewBox="0 0 20 20"><path d="M10 1a6 6 0 0 0-6 6c0 5 6 12 6 12s6-7 6-12a6 6 0 0 0-6-6z" fill="#fff"/><circle cx="10" cy="7" r="2.2" fill="var(--band)"/></svg>
        <div>Hotel am Birkenhain<br>Lindenweg 7 | 54531 Manderscheid</div>
      </div>
    </div>
    <div class="abs" style="left:300px;top:100px">
      <div class="info-line"><svg class="icon" viewBox="0 0 20 20"><path d="M5 2l3 4-2 2a11 11 0 0 0 6 6l2-2 4 3-2 3C9 18 2 11 2 4z" fill="#fff"/></svg>0049 170 555 0182</div>
      <div class="info-line" style="margin-top:8px"><svg class="icon" viewBox="0 0 20 20"><rect x="2" y="4" width="16" height="12" fill="#fff"/><path d="M2 4l8 7 8-7" fill="none" stroke="var(--band)" stroke-width="1.5"/></svg>hotelbirkenhain@post-netz.de</div>
    </div>
    <div class="abs" style="left:560px;top:100px">
      <div class="info-line" style="align-items:flex-start">
        <svg class="icon" viewBox="0 0 20 20"><circle cx="10" cy="10" r="8" fill="none" stroke="#fff" stroke-width="1.6"/><ellipse cx="10" cy="10" rx="3.5" ry="8" fill="none" stroke="#fff" stroke-width="1.4"/><path d="M2 10h16" stroke="#fff" stroke-width="1.4"/></svg>
        <div>Besuchen Sie uns online:<br>www.hotelambirkenhain.com</div>
      </div>
    </div>
  </div>
  <div class="pill" style="left:280px;top:912px">Hotel am Birkenhain</div>
  <div class="badge" style="left:600px;top:840px;width:130px;height:130px"><svg viewBox="-50 -50 100 100"><g fill="var(--green)"><rect x="-36" y="-36" width="72" height="72"/><rect x="-36" y="-36" width="72" height="72" transform="rotate(30)"/><rect x="-36" y="-36" width="72" height="72" transform="rotate(60)"/></g></svg><div class="badge__text" style="font-size:14px">Wir freuen<br>uns auf Ihren<br>Besuch!</div></div>
</section>

</body>
</html>
```